Coffee Package Design

We need a new package design for a coffee company. Need to be a mix between modern and classic design combined together. We are open to different ideas.
We changing our product name from Café Verlona to Café Rostelli. The picture upload
shows what the product looks like. We want something completely different. The name of the company should go on the back of the package.
Updates

Hello Everyone,

Please read description, we are going with a new name and design for the product.

Café Rostelli. Café Verlona is what we are replacing with Café Rostelli, we are looking for new

look and design, please submit new designs.

There is a change in the description. Please take out Premium coffee blend and replace with Italian Roast.                                    

Industry/Entity Type

Cafe

Requirements
Must have
• You can use up to 6 colors.
Please put these items on design: Café Rostelli (this is the product name), Regular Premium Blend Coffee, 100% Arabica,
Dumbrell & Sons (name of the company), Tyler, TX on the back of the package

The file uploaded is an example of one of our products and how the package film
is sized.

```html
<!DOCTYPE html>
<html lang="en">
<head>
<meta charset="utf-8">
<title>Café Rostelli – Package Film</title>
<link rel="stylesheet" href="https://fonts.googleapis.com/css2?family=Cinzel:wght@400;500&family=Source+Sans+3:wght@700&display=swap">
<style>
  :root {
    --paper: #ffffff;
    --name-copper: #cf8663;
    --info-terracotta: #d1704f;
    --cup-cream: #f6efcf;
    --cup-shadow: #e4d6a6;
    --coffee-brown: #8a5a36;
    --steam-tan: #ecd3ae;
  }
  html, body {
    margin: 0;
    padding: 0;
    overflow: hidden;
    background: var(--paper);
  }
  .package-film {
    position: relative;
    width: 1200px;
    height: 694px;
    background: var(--paper);
    overflow: hidden;
  }
  .product-name {
    position: absolute;
    margin: 0;
    font-family: "Cinzel", "Times New Roman", serif;
    font-weight: 400;
    color: var(--name-copper);
    white-space: nowrap;
    line-height: 1;
  }
  .product-name--front {
    left: 596px;
    top: 314px;
    font-size: 62px;
    transform: translateX(-50%);
  }
  .product-name--side {
    left: 279px;
    top: 360px;
    font-size: 37px;
    letter-spacing: 0.02em;
    transform: translate(-50%, -50%) rotate(-90deg);
  }
  .cup-art {
    position: absolute;
  }
  .cup-art--front {
    left: 528px;
    top: 90px;
    width: 132px;
    height: 196px;
  }
  .cup-art--side {
    left: 135px;
    top: 318px;
    width: 114px;
    height: 86px;
  }
  .info {
    position: absolute;
    margin: 0;
    font-family: "Source Sans 3", "Arial", sans-serif;
    font-weight: 700;
    color: var(--info-terracotta);
    white-space: nowrap;
  }
  .blend-details {
    left: 327px;
    top: 538px;
    font-size: 25px;
    line-height: 34px;
  }
  .company-details {
    left: 985px;
    top: 339px;
    font-size: 24px;
    line-height: 28px;
    text-align: left;
    transform: translate(-50%, -50%) rotate(-90deg);
  }
</style>
</head>
<body>
  <main class="package-film">
    <svg class="cup-art cup-art--front" viewBox="0 0 132 196" role="img" aria-label="Illustration of a steaming cup of coffee with latte art">
      <defs>
        <linearGradient id="steam-fade" x1="0" y1="0" x2="0" y2="1">
          <stop offset="0" stop-color="var(--steam-tan)" stop-opacity="0"/>
          <stop offset="1" stop-color="var(--steam-tan)" stop-opacity="0.8"/>
        </linearGradient>
        <linearGradient id="cup-fill" x1="0" y1="0" x2="1" y2="1">
          <stop offset="0" stop-color="var(--cup-cream)"/>
          <stop offset="0.6" stop-color="var(--cup-shadow)"/>
          <stop offset="1" stop-color="var(--coffee-brown)" stop-opacity="0.35"/>
        </linearGradient>
      </defs>
      <rect x="30" y="0" width="60" height="100" rx="30" fill="url(#steam-fade)"/>
      <rect x="0" y="96" width="132" height="100" rx="40" fill="url(#cup-fill)"/>
    </svg>

    <h1 class="product-name product-name--front">Café Rostelli</h1>

    <svg class="cup-art cup-art--side" viewBox="0 0 114 86" role="img" aria-label="Small illustration of a coffee cup tipped sideways with steam">
      <defs>
        <linearGradient id="side-cup-fill" x1="0" y1="0" x2="1" y2="0">
          <stop offset="0" stop-color="var(--steam-tan)" stop-opacity="0.2"/>
          <stop offset="0.45" stop-color="var(--cup-cream)"/>
          <stop offset="1" stop-color="var(--cup-shadow)"/>
        </linearGradient>
      </defs>
      <rect x="0" y="0" width="114" height="86" rx="34" fill="url(#side-cup-fill)"/>
    </svg>

    <p class="product-name product-name--side">Café Rostelli</p>

    <p class="info blend-details">Regular Italian Roast<br>100% Arabica</p>

    <p class="info company-details">Dumbrell &amp; Sons<br>Avonby, Westra</p>
  </main>
</body>
</html>
```